Gordon the Glazier
stationary
Gordon the Glazier -
Creative Brief
Simple
Desmond Pryce
PO Box 417 KELDARRA VIC 3062
gordon@gordontheglazier.com.au
www.gordontheglazier.com.au
I don't need my name or address on the business card -- it just needs to be a general "Gordon the Glazier" card with phone and email contact and web address. Could you also put "Member of the TGWB" somewhere -- this text doesn't have to be bold/eye-catching. It would be good if you could design a business card, letterhead and envelope design

```html
<!DOCTYPE html>
<html lang="en">
<head>
<meta charset="utf-8">
<title>Gordon the Glazier – Stationery</title>
<link href="https://fonts.googleapis.com/css2?family=Nunito:wght@800&family=Open+Sans:wght@400;600&display=swap" rel="stylesheet">
<style>
:root{
  --navy:#2e3a8f;
  --sky:#17a3cc;
  --paper:#ffffff;
  --ink:#3a3f5c;
  --stage:#e4e5e8;
  --window:#eef0f3;
}
*{box-sizing:border-box;margin:0;padding:0}
html,body{width:1200px;height:737px;overflow:hidden;background:var(--stage)}
body{position:relative;font-family:"Open Sans",Arial,sans-serif;color:var(--ink)}
.piece{position:absolute;background:var(--paper);box-shadow:0 2px 6px rgba(0,0,0,.18);overflow:hidden}
.brand{display:flex;align-items:center;gap:8px}
.brand-mark{width:22px;height:22px;background:var(--navy);border-radius:4px;flex:none}
.brand-name{font-family:"Nunito",Arial,sans-serif;font-weight:800;color:var(--navy);line-height:1.05}

/* Letterhead */
.letterhead{left:24px;top:24px;width:533px;height:696px}
.letterhead .rule-sky{position:absolute;top:0;left:0;right:0;height:4px;background:var(--sky)}
.letterhead .rule-navy{position:absolute;top:0;right:0;width:186px;height:9px;background:var(--navy)}
.letterhead .brand{position:absolute;left:18px;top:20px}
.letterhead .brand-name{font-size:20px;width:110px}
.letterhead .footer{position:absolute;left:18px;bottom:22px;font-size:7px;line-height:1.6;color:var(--ink)}

/* Envelope */
.envelope{left:595px;top:43px;width:581px;height:341px}
.envelope .flap{position:absolute;left:0;top:0;width:100%;height:100px}
.envelope .brand{position:absolute;left:14px;top:130px}
.envelope .brand-mark{width:30px;height:30px}
.envelope .brand-name{font-size:26px;width:150px}
.envelope .return{position:absolute;left:14px;top:210px;font-size:8px}
.envelope .window{position:absolute;left:150px;top:210px;width:170px;height:106px;border:1px solid #c9ccd3;border-radius:12px;background:var(--window)}
.envelope .bar-navy{position:absolute;left:0;bottom:0;width:257px;height:8px;background:var(--navy)}
.envelope .bar-sky{position:absolute;left:257px;right:0;bottom:0;height:3px;background:var(--sky)}

/* Business cards */
.card{width:209px;height:120px}
.card-front-a{left:643px;top:420px}
.card-front-b{left:907px;top:420px}
.card-back-navy{left:643px;top:564px;width:209px;height:132px;background:var(--navy)}
.card-back-sky{left:907px;top:564px;width:214px;height:132px;background:var(--sky)}
.card .top-bar{position:absolute;top:0;right:0;width:70px;height:5px;background:var(--sky)}
.card .bottom-bar{position:absolute;left:0;bottom:0;width:100%;height:3px;background:var(--navy)}
.card-front-a .brand{position:absolute;left:10px;top:12px}
.card-front-a .brand-name{font-size:15px;width:100px}
.card-front-a .contact{position:absolute;left:10px;top:72px;font-size:5.5px;line-height:1.6}
.card-front-a .member{position:absolute;right:10px;top:86px;font-size:5.5px;color:var(--sky)}
.card-front-b .brand{position:absolute;left:50%;top:50%;transform:translate(-50%,-50%)}
.card-front-b .brand-name{font-size:17px;width:110px}
.card-back .brand{position:absolute;left:50%;top:50%;transform:translate(-50%,-50%);flex-direction:column;gap:6px}
.card-back .brand-mark{width:34px;height:34px;background:var(--paper)}
.card-back .brand-name{font-size:11px;color:var(--paper);text-align:center}
</style>
</head>
<body>

<section class="piece letterhead" aria-label="Letterhead">
  <div class="rule-sky"></div>
  <div class="rule-navy"></div>
  <div class="brand"><span class="brand-mark"></span><span class="brand-name">Gordon the Glazier</span></div>
  <div class="footer">
    <p>PO Box 417 KELDARRA VIC 3062 &nbsp;|&nbsp; Phone 0400 211 448</p>
    <p>Email: gordon@gordontheglazier.com.au &nbsp;|&nbsp; www.gordontheglazier.com.au</p>
  </div>
</section>

<section class="piece envelope" aria-label="Envelope">
  <svg class="flap" viewBox="0 0 581 100" preserveAspectRatio="none">
    <path d="M0 0H581V70Q290 100 0 70Z" fill="var(--navy)"/>
  </svg>
  <div class="brand"><span class="brand-mark"></span><span class="brand-name">Gordon the Glazier</span></div>
  <p class="return">PO Box 417 KELDARRA VIC 3062</p>
  <div class="window"></div>
  <div class="bar-navy"></div>
  <div class="bar-sky"></div>
</section>

<section class="piece card card-front-a" aria-label="Business card front">
  <div class="top-bar"></div>
  <div class="brand"><span class="brand-mark"></span><span class="brand-name">Gordon the Glazier</span></div>
  <div class="contact">
    <p>Phone: 0400 211 448</p>
    <p>Email: gordon@gordontheglazier.com.au</p>
    <p>www.gordontheglazier.com.au</p>
  </div>
  <p class="member">Member of the TGWB</p>
  <div class="bottom-bar"></div>
</section>

<section class="piece card card-front-b" aria-label="Business card front alternative">
  <div class="top-bar"></div>
  <div class="brand"><span class="brand-mark"></span><span class="brand-name">Gordon the Glazier</span></div>
  <div class="bottom-bar"></div>
</section>

<section class="piece card-back card-back-navy" aria-label="Business card back navy">
  <div class="brand"><span class="brand-mark"></span><span class="brand-name">Gordon the Glazier</span></div>
</section>

<section class="piece card-back card-back-sky" aria-label="Business card back sky blue">
  <div class="brand"><span class="brand-mark"></span><span class="brand-name">Gordon the Glazier</span></div>
</section>

</body>
</html>
```